Summit Grading a Builders LLC business card

My current business card is very plain. it has my logo and contact information. I woud like something that stands out from the rest. please take a look at my website to see about my company.

Compayt Name - Summit Grading And Builders
Owner - Martin Kowalczyk
Business Address
Business Website - www.summitgradingandbuilders.example
Email - Summitgradingandbuilders@mailbox.example
Phone - 555-214-7390
Fax - 555-806-3127

Target Market(s)

Everyone age tang is 18 - 85

Industry/Entity Type

Business

Contact Information for Business Card

Nice and professional all in one.

Font styles to use
Serif
Other font styles liked:
• Up to you

Requirements
Must have
• All contact info. The design is up to you.
Nice to have
• All the contact info the design is up to you
Should not have
• I don't have any

```html
<!DOCTYPE html>
<html lang="en">
<head>
<meta charset="utf-8">
<title>Summit Grading &amp; Builders LLC – Business Card</title>
<link rel="stylesheet" href="https://fonts.googleapis.com/css2?family=Open+Sans:wght@400;600&family=Roboto+Slab:wght@400;800&family=Ubuntu:wght@700&display=swap">
<style>
  :root {
    --page: #e4e5e7;
    --ink: #141414;
    --ink-soft: #3a3a3a;
    --paper: #ffffff;
    --accent: #f7941d;
    --silver: #cfcfcf;
    --rule: #9a9a9a;
  }
  * { box-sizing: border-box; margin: 0; padding: 0; }
  html, body {
    width: 1200px; height: 1000px; overflow: hidden;
    background: var(--page);
  }
  .sheet { position: relative; width: 1200px; height: 1000px; }
  .card {
    position: absolute; left: 220px;
    width: 760px; height: 434px;
    border-radius: 28px; overflow: hidden;
    background: var(--paper);
    box-shadow: 0 10px 30px rgba(0,0,0,.18);
  }
  .card-front { top: 48px; }
  .card-back  { top: 518px; background: var(--ink); }
  .card-shapes { position: absolute; inset: 0; width: 100%; height: 100%; }

  /* front */
  .front-company {
    position: absolute; left: 60px; right: 40px; top: 30px;
    font-family: "Roboto Slab", serif; font-weight: 400;
    font-size: 28px; letter-spacing: 1px; text-transform: uppercase;
    color: var(--silver); white-space: nowrap; text-align: right;
  }
  .owner { position: absolute; left: 40px; top: 200px; }
  .owner-name {
    font-family: "Ubuntu", sans-serif; font-weight: 700;
    font-size: 24px; color: var(--ink-soft); text-transform: uppercase;
    line-height: 1.1; white-space: nowrap;
  }
  .owner-role {
    font-family: "Open Sans", sans-serif; font-size: 20px;
    color: var(--accent); line-height: 1.3;
  }
  .divider {
    position: absolute; left: 326px; top: 190px;
    width: 2px; height: 140px; background: var(--rule);
  }
  .contact-list {
    position: absolute; left: 344px; top: 188px;
    list-style: none;
    font-family: "Open Sans", sans-serif; font-size: 16px;
    color: var(--ink-soft); line-height: 26px;
  }
  .contact-list li { display: flex; align-items: center; gap: 9px; white-space: nowrap; }
  .contact-list .no-icon { padding-left: 23px; }
  .contact-icon { width: 14px; height: 14px; flex: none; fill: var(--accent); }

  /* back */
  .back-company {
    position: absolute; left: 0; right: 0; top: 136px;
    text-align: center;
    font-family: "Roboto Slab", serif; font-weight: 800;
    font-size: 42px; line-height: 1.05; letter-spacing: 1px;
    text-transform: uppercase; color: var(--ink-soft);
  }
  .web-tag {
    position: absolute; left: 236px; top: 236px;
    padding: 4px 14px;
    background: var(--accent); color: var(--paper);
    font-family: "Open Sans", sans-serif; font-size: 16px; font-weight: 600;
  }
</style>
</head>
<body>
<main class="sheet">

  <section class="card card-front" aria-label="Business card front">
    <svg class="card-shapes" viewBox="0 0 760 434" aria-hidden="true">
      <polygon points="0,0 760,0 760,168 0,72" fill="var(--ink)"/>
      <polygon points="0,72 760,168 760,176 0,80" fill="var(--accent)"/>
      <polygon points="0,404 50,404 64,388 78,404 760,404 760,434 0,434" fill="var(--accent)"/>
    </svg>

    <h1 class="front-company">Summit Grading &amp; Builders LLC</h1>

    <div class="owner">
      <h2 class="owner-name">Martin Kowalczyk</h2>
      <p class="owner-role">Owner</p>
    </div>

    <div class="divider"></div>

    <ul class="contact-list">
      <li class="no-icon">4870 Ridge Avenue, Millbrook,</li>
      <li class="no-icon">NY, United States</li>
      <li>
        <svg class="contact-icon" viewBox="0 0 16 16"><path d="M3.5 1l2.5 3-1.5 2c1 2 3 4 5 5l2-1.5 3 2.5-1.5 2.5C7 15 1 9 1 2.5z"/></svg>
        555-214-7390
      </li>
      <li>
        <svg class="contact-icon" viewBox="0 0 16 16"><rect x="4" y="1" width="8" height="5"/><rect x="1" y="6" width="14" height="7" rx="1"/><rect x="4" y="11" width="8" height="4"/></svg>
        555-806-3127
      </li>
      <li>
        <svg class="contact-icon" viewBox="0 0 16 16"><path d="M1 3h14v10H1z M1 3l7 6 7-6" stroke="var(--paper)" stroke-width="1"/></svg>
        Summitgradingandbuilders@mailbox.example
      </li>
      <li>
        <svg class="contact-icon" viewBox="0 0 16 16"><circle cx="8" cy="8" r="7"/><path d="M1 8h14M8 1c-3 3-3 11 0 14M8 1c3 3 3 11 0 14" stroke="var(--paper)" stroke-width="1" fill="none"/></svg>
        www.summitgradingandbuilders.example
      </li>
    </ul>
  </section>

  <section class="card card-back" aria-label="Business card back">
    <svg class="card-shapes" viewBox="0 0 760 434" aria-hidden="true">
      <polygon points="0,64 760,120 760,300 0,244" fill="var(--paper)"/>
      <polygon points="0,244 760,300 760,308 0,252" fill="var(--accent)"/>
    </svg>

    <h2 class="back-company">Summit Grading<br>&amp; Builders LLC</h2>
    <p class="web-tag">www.summitgradingandbuilders.example</p>
  </section>

</main>
</body>
</html>
```